Modern Business Card

Modern professional business card with more than just logo and demographic info. Something memorable.

We are a trendy/modern chiropractic group with an emphasis on neurology, hence the minimalist-type brain logo. We want to convey that modern and technical aspect with professionalism and the elite nature of our practice environment.

```html
<!DOCTYPE html>
<html lang="en">
<head>
<meta charset="utf-8">
<title>Meridian Spine – Business Card</title>
<link href="https://fonts.googleapis.com/css2?family=EB+Garamond:wght@500&family=Montserrat:wght@800&family=Open+Sans:wght@400&display=swap" rel="stylesheet">
<style>
  :root {
    --backdrop: #cfcdcb;
    --paper: #f7f7f8;
    --brand-blue: #3a78c0;
    --ink: #1b1b1b;
  }
  * { margin: 0; padding: 0; box-sizing: border-box; }
  html, body { width: 1200px; height: 892px; overflow: hidden; }
  body {
    background: var(--backdrop);
    display: flex;
    flex-direction: column;
    align-items: center;
    justify-content: center;
    gap: 56px;
  }
  .card {
    position: relative;
    width: 620px;
    height: 354px;
    background: var(--paper);
    overflow: hidden;
    box-shadow: 0 2px 6px rgba(0,0,0,0.12);
  }
  /* Front */
  .brand-mark {
    position: absolute;
    left: 250px;
    top: 82px;
    display: flex;
    align-items: center;
    gap: 12px;
  }
  .brand-mark .dot {
    width: 30px; height: 30px;
    border-radius: 50%;
    background: var(--brand-blue);
  }
  .brand-mark .name {
    font-family: "EB Garamond", serif;
    font-weight: 500;
    font-size: 34px;
    letter-spacing: 1px;
    color: var(--ink);
    text-transform: uppercase;
    line-height: 1;
  }
  .practice-name {
    position: absolute;
    left: 56px;
    top: 200px;
    color: var(--brand-blue);
  }
  .practice-name strong {
    display: block;
    font-family: "Montserrat", sans-serif;
    font-weight: 800;
    font-size: 22px;
    line-height: 1.15;
    text-transform: uppercase;
  }
  .practice-name span {
    display: block;
    font-family: "Open Sans", sans-serif;
    font-size: 18px;
    margin-top: 4px;
  }
  .contact {
    position: absolute;
    left: 365px;
    top: 198px;
    font-family: "Open Sans", sans-serif;
    font-size: 15px;
    line-height: 1.3;
    color: var(--brand-blue);
  }
  .contact .phone { margin-top: 16px; }
  /* Back */
  .wave-field {
    position: absolute;
    inset: 0;
  }
  .vertical-name {
    position: absolute;
    right: 56px;
    top: 22px;
    height: 170px;
    writing-mode: vertical-rl;
    transform: rotate(180deg);
    display: flex;
    flex-direction: column;
    justify-content: flex-start;
    font-family: "EB Garamond", serif;
    font-weight: 500;
    color: var(--brand-blue);
    text-transform: uppercase;
    line-height: 1;
  }
  .vertical-name .line-main { font-size: 28px; letter-spacing: 1px; }
  .vertical-name .line-sub { font-size: 15px; letter-spacing: 2px; margin-right: 2px; }
</style>
</head>
<body>
  <section class="card card-front" aria-label="Card front">
    <div class="brand-mark">
      <span class="dot"></span>
      <span class="name">Meridian Spine</span>
    </div>
    <div class="practice-name">
      <strong>Meridian<br>Spine</strong>
      <span>Fairhaven</span>
    </div>
    <div class="contact">
      <p>218 Elm Park Rd,<br>Fairhaven, OH 43000</p>
      <p class="phone">TEL: 555-014-2270</p>
    </div>
  </section>

  <section class="card card-back" aria-label="Card back">
    <svg class="wave-field" width="620" height="354" viewBox="0 0 620 354" role="img" aria-label="Decorative pattern of rounded vertical blue strokes rising across the lower card">
      <polygon points="0,120 300,165 470,210 620,220 620,354 0,354" fill="var(--brand-blue)"/>
    </svg>
    <div class="vertical-name">
      <span class="line-main">Meridian</span>
      <span class="line-sub">Spine</span>
    </div>
  </section>
</body>
</html>
```